i am creating an a new cold brew coffee and need a standard format for 5 different flavours. the PDF with 5 colours is what i created as a format and the one page PDF is the style i like but am happy yo move away from it.. the images are the style i like

i am looking for a nice clean tidy but standard out label that will pop off a brown paper backing.

Target Market(s)

18-40 Yr old coffee lovers wanting a high end cold brew coffee

Font styles to use
Serif
Sans Serif

Colors

Designer to choose colors to be used in the design.

Requirements
Must have
• i want a standard format that a component can change colour with flavours, brown paper background. i need the nutritional content box at the back ( as per PDF ) and i would like the text added also, as this is a description of the product
Nice to have
• i like the tidy clinical look of the font pharma bold condensed
• the PDF's show the flavours.. the one with a brown background is something i have seen that i like and the images are the styles i like .

```html
<!DOCTYPE html>
<html lang="en">
<head>
<meta charset="utf-8">
<title>Kestrel Brews – Sparkling Cold Brew Label Set</title>
<link rel="stylesheet" href="https://fonts.googleapis.com/css2?family=Anton&family=Archivo+Black&family=Roboto+Condensed:wght@400;700&family=Yellowtail&display=swap">
<style>
  :root{
    --kraft:#c8a77b;
    --espresso:#5b3f33;
    --bean:#7d5e48;
    --coffee-red:#f0401f;
    --ink:#1c1a19;
    --white:#ffffff;
    --badge-red:#d9283a;
    --badge-blue:#2a4d8e;
    --vegan:#d98a1e;
  }
  *{box-sizing:border-box;margin:0;padding:0}
  html,body{width:990px;height:1200px;overflow:hidden;background:var(--white)}
  .sheet{position:relative;width:990px;height:1200px}
  .flavour-row{position:absolute;left:0;width:990px;height:215px}
  .flavour-row.ginger{top:10px;--flavour:#ff3c0f;--sub:#ff3c0f}
  .flavour-row.blackberry{top:250px;--flavour:#c597c9;--sub:#9c63a6}
  .flavour-row.chocolate{top:490px;--flavour:#5c2a2a;--sub:#5c2a2a}
  .flavour-row.coconut{top:730px;--flavour:#9ccd5c;--sub:#5f9a26}
  .flavour-row.citrus{top:970px;--flavour:#f8c12a;--sub:#f8c12a}

  /* front label */
  .label-front{position:absolute;left:12px;top:0;width:465px;height:215px;background:var(--kraft);overflow:hidden}
  .label-front > div{position:absolute}
  .gap-white{left:57px;top:0;width:8px;height:215px;background:var(--white)}
  .band-left{left:0;top:142px;width:57px;height:40px;background:var(--flavour)}
  .band-col{left:57px;top:142px;width:80px;height:40px;background:var(--white)}
  .coffee-col{left:65px;top:0;width:65px;height:215px;display:flex;align-items:center;justify-content:center}
  .coffee-vertical{font-family:"Anton",sans-serif;font-size:60px;color:var(--coffee-red);writing-mode:vertical-rl;transform:rotate(180deg);line-height:1;letter-spacing:1px}
  .rule-white{left:130px;top:0;width:4px;height:215px;background:var(--white)}
  .rule-accent{left:134px;top:0;width:3px;height:215px;background:var(--flavour)}
  .brand{left:158px;top:32px;width:180px;font-family:"Archivo Black",sans-serif;font-size:29px;line-height:34px;color:var(--ink);white-space:nowrap;z-index:2}
  .seal{left:345px;top:24px;width:100px;height:100px;border-radius:50%;background:var(--badge-red);border:6px solid var(--badge-blue);box-shadow:0 0 0 3px var(--white)}
  .subtitle{left:168px;top:104px;font-family:"Yellowtail",cursive;font-size:24px;line-height:30px;color:var(--sub);white-space:nowrap}
  .band-main{left:137px;top:142px;width:328px;height:40px;background:var(--flavour)}
  .flavour-name{left:164px;top:142px;width:244px;height:40px;line-height:40px;font-family:"Yellowtail",cursive;font-size:28px;color:var(--white);white-space:nowrap;overflow:hidden}
  .blackberry .flavour-name{font-size:24px}
  .volume{left:418px;top:147px;width:30px;height:30px;display:flex;align-items:center;justify-content:center}
  .volume::before{content:"";position:absolute;inset:3px;border:1.5px solid var(--white);transform:rotate(45deg);background:rgba(255,255,255,.15)}
  .volume span{position:relative;font-family:"Yellowtail",cursive;font-size:9px;color:var(--white)}
  .rule-under{left:137px;top:185px;width:328px;height:3px;background:var(--white)}
  .beans-front{left:137px;top:190px;width:328px;height:25px;background:var(--bean);opacity:.75}

  /* back label */
  .label-back{position:absolute;left:507px;top:0;width:464px;height:215px;background:var(--white);overflow:hidden}
  .label-back > div{position:absolute}
  .back-panel{left:0;top:0;width:464px;height:134px;background:var(--espresso)}
  .nutrition{left:10px;top:8px;width:130px;height:118px;background:var(--white);font-family:"Roboto Condensed",sans-serif;color:#3a2a22;padding:3px 4px}
  .nutrition .head{display:flex;font-size:5.5px;font-weight:700;line-height:6px;border-bottom:.6px solid #3a2a22;padding-bottom:2px}
  .nutrition .head span:first-child{width:64px}
  .nutrition .head span{width:32px}
  .nutrition .servings{display:flex;font-size:6px;line-height:10px;border-bottom:1px solid #3a2a22}
  .nutrition .servings span:first-child{width:64px}
  .nutrition .servings span{width:32px}
  .nutrition ul{list-style:none;font-size:5.3px;line-height:7.8px}
  .nutrition li{border-bottom:.5px solid #8a7a70;display:flex}
  .nutrition li span{width:64px;border-right:.5px solid #8a7a70}
  .nutrition .ingredients{font-size:5px;line-height:6.5px;margin-top:4px;border-top:.8px solid #3a2a22;padding-top:2px}
  .notice{left:150px;top:12px;width:108px;font-family:"Roboto Condensed",sans-serif;font-weight:700;font-size:5.6px;line-height:7px;color:var(--white);text-align:center;letter-spacing:.3px}
  .notice p{border-bottom:1px solid var(--white);padding-bottom:2px;margin-bottom:3px}
  .diet-badge{top:72px;width:42px;height:42px;border-radius:50%}
  .diet-badge.vegan{left:160px;background:var(--vegan)}
  .diet-badge.gluten{left:210px;background:var(--white);border-radius:8px}
  .story{left:267px;top:8px;width:186px;font-family:"Roboto Condensed",sans-serif;font-size:5.5px;line-height:6.8px;color:var(--white);text-align:justify}
  .story p{margin-bottom:5px}
  .story strong{font-weight:700}
  .story .release{font-size:6.5px;font-weight:700;margin-bottom:0}
  .story .release span{margin-left:14px}
  .coffee-word{left:12px;top:134px;height:54px;line-height:54px;font-family:"Anton",sans-serif;font-size:42px;color:var(--coffee-red);letter-spacing:1px}
  .coffee-word::after{content:"";position:absolute;left:0;right:0;bottom:8px;height:2px;background:var(--coffee-red)}
  .back-flavour{left:160px;top:134px;width:300px;height:54px;line-height:54px;font-family:"Yellowtail",cursive;font-size:34px;color:var(--flavour);white-space:nowrap;overflow:hidden}
  .blackberry .back-flavour{font-size:29px}
  .beans-back{left:0;top:188px;width:464px;height:27px;background:var(--espresso)}
</style>
</head>
<body>
<main class="sheet">

  <!-- Sparkling Ginger -->
  <section class="flavour-row ginger">
    <div class="label-front">
      <div class="gap-white"></div>
      <div class="band-left"></div>
      <div class="band-col"></div>
      <div class="coffee-col"><span class="coffee-vertical">Coffee</span></div>
      <div class="rule-white"></div>
      <div class="rule-accent"></div>
      <div class="seal" role="img" aria-label="Australian made and owned seal"></div>
      <div class="brand">KESTREL<br>BREWS</div>
      <div class="band-main"></div>
      <div class="flavour-name">Sparkling Ginger</div>
      <div class="volume"><span>330ml</span></div>
      <div class="rule-under"></div>
      <div class="beans-front" role="img" aria-label="Coffee bean pattern"></div>
    </div>
    <div class="label-back">
      <div class="back-panel"></div>
      <div class="nutrition">
        <div class="head"><span>NUTRITIONAL INFORMATION</span><span>PER SERV.</span><span>PER 100G</span></div>
        <div class="servings"><span>SERVINGS:</span><span>1</span><span>330ml</span></div>
        <ul><li><span>Energy</span></li><li><span>Protein</span></li><li><span>Fat, Total</span></li><li><span>Saturated</span></li><li><span>Carbs</span></li><li><span>Sugars</span></li><li><span>Sodium</span></li></ul>
        <p class="ingredients">All Organic Ingredients: Cold Brew coffee, Arabica Beans, Raw Coconut Nectar, Ginger 4%</p>
      </div>
      <div class="notice"><p>*KEEP REFRIGERATED AFTER OPENING &amp; CONSUME WITHIN 2 DAYS FROM OPENING</p><p>*PLEASE DO NOT SHAKE</p></div>
      <div class="diet-badge vegan" role="img" aria-label="Naturally vegan badge"></div>
      <div class="diet-badge gluten" role="img" aria-label="Gluten free badge"></div>
      <div class="story">
        <p>Kestrel Brews made this Cold brew coffee to make you think clearer, feel motivated and to just be a better person. We wont claim any responsibility for the achievements you make while drinking our brews, that brilliance was always about you, we just helped you bring it out.</p>
        <p>We know that if you have finished the bottle you will be feeling too good to be reading this label in its entirety. So we will finish it here so you can continue on your motivated way.</p>
        <p>Want to contact us? Sure do it here: <strong>www.kestrelbrews.com.au</strong> Or here: <strong>42 Tannery Lane, Newtown NSW 2042</strong> or on this 0400 000 111</p>
        <p class="release">World first release: <span>Call 0400 123 456</span></p>
        <p>For distribution enquiries.</p>
      </div>
      <div class="coffee-word">Coffee</div>
      <div class="back-flavour">Sparkling Ginger</div>
      <div class="beans-back" role="img" aria-label="Coffee bean pattern"></div>
    </div>
  </section>

  <!-- Sparkling Blackberry -->
  <section class="flavour-row blackberry">
    <div class="label-front">
      <div class="gap-white"></div>
      <div class="band-left"></div>
      <div class="band-col"></div>
      <div class="coffee-col"><span class="coffee-vertical">Coffee</span></div>
      <div class="rule-white"></div>
      <div class="rule-accent"></div>
      <div class="seal" role="img" aria-label="Australian made and owned seal"></div>
      <div class="brand">KESTREL<br>BREWS</div>
      <div class="subtitle">Cold Brew</div>
      <div class="band-main"></div>
      <div class="flavour-name">Sparkling Blackberry</div>
      <div class="volume"><span>330ml</span></div>
      <div class="rule-under"></div>
      <div class="beans-front" role="img" aria-label="Coffee bean pattern"></div>
    </div>
    <div class="label-back">
      <div class="back-panel"></div>
      <div class="nutrition">
        <div class="head"><span>NUTRITIONAL INFORMATION</span><span>PER SERV.</span><span>PER 100G</span></div>
        <div class="servings"><span>SERVINGS:</span><span>1</span><span>330ml</span></div>
        <ul><li><span>Energy</span></li><li><span>Protein</span></li><li><span>Fat, Total</span></li><li><span>Saturated</span></li><li><span>Carbs</span></li><li><span>Sugars</span></li><li><span>Sodium</span></li></ul>
        <p class="ingredients">All Organic Ingredients: Cold Brew coffee, Arabica Beans, Raw Coconut Nectar, Ginger 4%</p>
      </div>
      <div class="notice"><p>*KEEP REFRIGERATED AFTER OPENING &amp; CONSUME WITHIN 2 DAYS FROM OPENING</p><p>*PLEASE DO NOT SHAKE</p></div>
      <div class="diet-badge vegan" role="img" aria-label="Naturally vegan badge"></div>
      <div class="diet-badge gluten" role="img" aria-label="Gluten free badge"></div>
      <div class="story">
        <p>Kestrel Brews made this Cold brew coffee to make you think clearer, feel motivated and to just be a better person. We wont claim any responsibility for the achievements you make while drinking our brews, that brilliance was always about you, we just helped you bring it out.</p>
        <p>We know that if you have finished the bottle you will be feeling too good to be reading this label in its entirety. So we will finish it here so you can continue on your motivated way.</p>
        <p>Want to contact us? Sure do it here: <strong>www.kestrelbrews.com.au</strong> Or here: <strong>42 Tannery Lane, Newtown NSW 2042</strong> or on this 0400 000 111</p>
        <p class="release">World first release: <span>Call 0400 123 456</span></p>
        <p>For distribution enquiries.</p>
      </div>
      <div class="coffee-word">Coffee</div>
      <div class="back-flavour">Sparkling Blackberry</div>
      <div class="beans-back" role="img" aria-label="Coffee bean pattern"></div>
    </div>
  </section>

  <!-- Sparkling Chocolate -->
  <section class="flavour-row chocolate">
    <div class="label-front">
      <div class="gap-white"></div>
      <div class="band-left"></div>
      <div class="band-col"></div>
      <div class="coffee-col"><span class="coffee-vertical">Coffee</span></div>
      <div class="rule-white"></div>
      <div class="rule-accent"></div>
      <div class="seal" role="img" aria-label="Australian made and owned seal"></div>
      <div class="brand">KESTREL<br>BREWS</div>
      <div class="subtitle">Cold Brew</div>
      <div class="band-main"></div>
      <div class="flavour-name">Sparkling Chocolate</div>
      <div class="volume"><span>330ml</span></div>
      <div class="rule-under"></div>
      <div class="beans-front" role="img" aria-label="Coffee bean pattern"></div>
    </div>
    <div class="label-back">
      <div class="back-panel"></div>
      <div class="nutrition">
        <div class="head"><span>NUTRITIONAL INFORMATION</span><span>PER SERV.</span><span>PER 100G</span></div>
        <div class="servings"><span>SERVINGS:</span><span>1</span><span>330ml</span></div>
        <ul><li><span>Energy</span></li><li><span>Protein</span></li><li><span>Fat, Total</span></li><li><span>Saturated</span></li><li><span>Carbs</span></li><li><span>Sugars</span></li><li><span>Sodium</span></li></ul>
        <p class="ingredients">All Organic Ingredients: Cold Brew coffee, Arabica Beans, Raw Coconut Nectar, Ginger 4%</p>
      </div>
      <div class="notice"><p>*KEEP REFRIGERATED AFTER OPENING &amp; CONSUME WITHIN 2 DAYS FROM OPENING</p><p>*PLEASE DO NOT SHAKE</p></div>
      <div class="diet-badge vegan" role="img" aria-label="Naturally vegan badge"></div>
      <div class="diet-badge gluten" role="img" aria-label="Gluten free badge"></div>
      <div class="story">
        <p>Kestrel Brews made this Cold brew coffee to make you think clearer, feel motivated and to just be a better person. We wont claim any responsibility for the achievements you make while drinking our brews, that brilliance was always about you, we just helped you bring it out.</p>
        <p>We know that if you have finished the bottle you will be feeling too good to be reading this label in its entirety. So we will finish it here so you can continue on your motivated way.</p>
        <p>Want to contact us? Sure do it here: <strong>www.kestrelbrews.com.au</strong> Or here: <strong>42 Tannery Lane, Newtown NSW 2042</strong> or on this 0400 000 111</p>
        <p class="release">World first release: <span>Call 0400 123 456</span></p>
        <p>For distribution enquiries.</p>
      </div>
      <div class="coffee-word">Coffee</div>
      <div class="back-flavour">Sparkling Chocolate</div>
      <div class="beans-back" role="img" aria-label="Coffee bean pattern"></div>
    </div>
  </section>

  <!-- Sparkling Coconut -->
  <section class="flavour-row coconut">
    <div class="label-front">
      <div class="gap-white"></div>
      <div class="band-left"></div>
      <div class="band-col"></div>
      <div class="coffee-col"><span class="coffee-vertical">Coffee</span></div>
      <div class="rule-white"></div>
      <div class="rule-accent"></div>
      <div class="seal" role="img" aria-label="Australian made and owned seal"></div>
      <div class="brand">KESTREL<br>BREWS</div>
      <div class="subtitle">Nectar Cold</div>
      <div class="band-main"></div>
      <div class="flavour-name">Sparkling Coconut</div>
      <div class="volume"><span>330ml</span></div>
      <div class="rule-under"></div>
      <div class="beans-front" role="img" aria-label="Coffee bean pattern"></div>
    </div>
    <div class="label-back">
      <div class="back-panel"></div>
      <div class="nutrition">
        <div class="head"><span>NUTRITIONAL INFORMATION</span><span>PER SERV.</span><span>PER 100G</span></div>
        <div class="servings"><span>SERVINGS:</span><span>1</span><span>330ml</span></div>
        <ul><li><span>Energy</span></li><li><span>Protein</span></li><li><span>Fat, Total</span></li><li><span>Saturated</span></li><li><span>Carbs</span></li><li><span>Sugars</span></li><li><span>Sodium</span></li></ul>
        <p class="ingredients">All Organic Ingredients: Cold Brew coffee, Arabica Beans, Raw Coconut Nectar, Ginger 4%</p>
      </div>
      <div class="notice"><p>*KEEP REFRIGERATED AFTER OPENING &amp; CONSUME WITHIN 2 DAYS FROM OPENING</p><p>*PLEASE DO NOT SHAKE</p></div>
      <div class="diet-badge vegan" role="img" aria-label="Naturally vegan badge"></div>
      <div class="diet-badge gluten" role="img" aria-label="Gluten free badge"></div>
      <div class="story">
        <p>Kestrel Brews made this Cold brew coffee to make you think clearer, feel motivated and to just be a better person. We wont claim any responsibility for the achievements you make while drinking our brews, that brilliance was always about you, we just helped you bring it out.</p>
        <p>We know that if you have finished the bottle you will be feeling too good to be reading this label in its entirety. So we will finish it here so you can continue on your motivated way.</p>
        <p>Want to contact us? Sure do it here: <strong>www.kestrelbrews.com.au</strong> Or here: <strong>42 Tannery Lane, Newtown NSW 2042</strong> or on this 0400 000 111</p>
        <p class="release">World first release: <span>Call 0400 123 456</span></p>
        <p>For distribution enquiries.</p>
      </div>
      <div class="coffee-word">Coffee</div>
      <div class="back-flavour">Sparkling Coconut</div>
      <div class="beans-back" role="img" aria-label="Coffee bean pattern"></div>
    </div>
  </section>

  <!-- Sparkling Citrus -->
  <section class="flavour-row citrus">
    <div class="label-front">
      <div class="gap-white"></div>
      <div class="band-left"></div>
      <div class="band-col"></div>
      <div class="coffee-col"><span class="coffee-vertical">Coffee</span></div>
      <div class="rule-white"></div>
      <div class="rule-accent"></div>
      <div class="seal" role="img" aria-label="Australian made and owned seal"></div>
      <div class="brand">KESTREL<br>BREWS</div>
      <div class="band-main"></div>
      <div class="flavour-name">Sparkling Citrus</div>
      <div class="volume"><span>330ml</span></div>
      <div class="rule-under"></div>
      <div class="beans-front" role="img" aria-label="Coffee bean pattern"></div>
    </div>
    <div class="label-back">
      <div class="back-panel"></div>
      <div class="nutrition">
        <div class="head"><span>NUTRITIONAL INFORMATION</span><span>PER SERV.</span><span>PER 100G</span></div>
        <div class="servings"><span>SERVINGS:</span><span>1</span><span>330ml</span></div>
        <ul><li><span>Energy</span></li><li><span>Protein</span></li><li><span>Fat, Total</span></li><li><span>Saturated</span></li><li><span>Carbs</span></li><li><span>Sugars</span></li><li><span>Sodium</span></li></ul>
        <p class="ingredients">All Organic Ingredients: Cold Brew coffee, Arabica Beans, Raw Coconut Nectar, Ginger 4%</p>
      </div>
      <div class="notice"><p>*KEEP REFRIGERATED AFTER OPENING &amp; CONSUME WITHIN 2 DAYS FROM OPENING</p><p>*PLEASE DO NOT SHAKE</p></div>
      <div class="diet-badge vegan" role="img" aria-label="Naturally vegan badge"></div>
      <div class="diet-badge gluten" role="img" aria-label="Gluten free badge"></div>
      <div class="story">
        <p>Kestrel Brews made this Cold brew coffee to make you think clearer, feel motivated and to just be a better person. We wont claim any responsibility for the achievements you make while drinking our brews, that brilliance was always about you, we just helped you bring it out.</p>
        <p>We know that if you have finished the bottle you will be feeling too good to be reading this label in its entirety. So we will finish it here so you can continue on your motivated way.</p>
        <p>Want to contact us? Sure do it here: <strong>www.kestrelbrews.com.au</strong> Or here: <strong>42 Tannery Lane, Newtown NSW 2042</strong> or on this 0400 000 111</p>
        <p class="release">World first release: <span>Call 0400 123 456</span></p>
        <p>For distribution enquiries.</p>
      </div>
      <div class="coffee-word">Coffee</div>
      <div class="back-flavour">Sparkling Citrus</div>
      <div class="beans-back" role="img" aria-label="Coffee bean pattern"></div>
    </div>
  </section>

</main>
</body>
</html>
```